TRVA Banner

This is for a generic retractable banner to be used anytime our group goes to large conferences and meetings. Please do not use any of the pictures from our website or reference Chicago or any of the events are attending. The plan is to use this banner anytime we go to a conference, set up at career fairs and have a table at a meeting.
We are the Crossward Surgical Results Alliance (TRVA) and I have included our logo. The website is: www.trva-net.org
Below are some qualities about our group, but please do not use these as a bullet point list on the banner. These are an overview of what we do at TRVA:
- Anesthesiologists / Anesthesiology
- Research, Quality and Education
- Large data repository
- Quality Champions
- Medical Researchers
- Perioperative Outcomes
- Innovators and trailblazers
- Medical research

```html
<!DOCTYPE html>
<html lang="en">
<head>
<meta charset="utf-8">
<title>TRVA Banner</title>
<link href="https://fonts.googleapis.com/css2?family=Open+Sans:wght@400;600;700;800&display=swap" rel="stylesheet">
<style>
:root{
  --page:#dedede;
  --white:#ffffff;
  --band:#7c7d7f;
  --field-top:#e6e7e8;
  --field-bottom:#cdd0d2;
  --green-hi:#9dc23d;--green-lo:#6f9a22;
  --olive-hi:#8bb045;--olive-lo:#5f8a2a;
  --gray-hi:#9a9b9d;--gray-lo:#6b6c6e;
  --orange-hi:#f7a13a;--orange-lo:#e07813;
  --brown-hi:#a7603a;--brown-lo:#7a3f22;
  --navy-hi:#356391;--navy-lo:#1c3f66;
  --blue-hi:#2a8ad0;--blue-lo:#0c63a8;
  --brand:#24507f;
  --brand-gray:#555759;
}
*{margin:0;padding:0;box-sizing:border-box}
html,body{width:1200px;height:900px;overflow:hidden;background:var(--page);font-family:"Open Sans",Arial,sans-serif}
.banner{position:absolute;left:422px;top:20px;width:355px;height:860px;background:var(--white);box-shadow:6px 8px 18px rgba(0,0,0,.22);overflow:hidden}
.hero{position:absolute;left:0;top:0;width:355px;height:333px}
.hero-photo{position:absolute;inset:0;background:linear-gradient(180deg,#3b6cb2 0%,#6a93c6 22%,#b9c3cc 33%,#d8b78e 40%,#4f7474 50%,#6f6658 62%,#8d5a45 74%,#3a4b57 88%,#2a3a46 100%)}
.hero-text{position:absolute;left:0;right:0;top:22px;text-align:center;color:var(--white);font-weight:800;text-shadow:0 1px 3px rgba(0,0,0,.3);line-height:1.15;white-space:nowrap}
.hero-text .line-a{font-size:21px;letter-spacing:.3px}
.hero-text .line-b{font-size:13.5px;margin-top:4px}
.hero-text .line-c{font-size:24px;margin-top:3px}
.band{position:absolute;left:0;top:333px;width:355px;height:37px;background:var(--band);color:var(--white);font-weight:800;font-size:19px;text-align:center;line-height:37px;letter-spacing:.3px}
.qualities{position:absolute;left:0;top:370px;width:355px;height:375px;background:linear-gradient(180deg,var(--field-top),var(--field-bottom))}
.hex{position:absolute;width:119px;height:101px;clip-path:polygon(25% 0,75% 0,100% 50%,75% 100%,25% 100%,0 50%);display:flex;align-items:center;justify-content:center;text-align:center;color:var(--white);font-size:13px;line-height:1.25;padding:0 10px;filter:drop-shadow(0 2px 2px rgba(0,0,0,.2))}
.hex-tight{font-size:11.5px;padding:0 4px;white-space:nowrap}
.green{background:linear-gradient(180deg,var(--green-hi),var(--green-lo))}
.olive{background:linear-gradient(180deg,var(--olive-hi),var(--olive-lo))}
.gray{background:linear-gradient(180deg,var(--gray-hi),var(--gray-lo))}
.orange{background:linear-gradient(180deg,var(--orange-hi),var(--orange-lo))}
.brown{background:linear-gradient(180deg,var(--brown-hi),var(--brown-lo))}
.navy{background:linear-gradient(180deg,var(--navy-hi),var(--navy-lo))}
.blue{background:linear-gradient(180deg,var(--blue-hi),var(--blue-lo))}
.footer{position:absolute;left:0;top:745px;width:355px;height:115px;display:flex;align-items:center;justify-content:center;gap:10px}
.brand-mark{width:28px;height:28px;background:var(--brand);margin-bottom:22px}
.brand-text{color:var(--brand);font-weight:700;line-height:1}
.brand-name{font-size:40px;letter-spacing:6px}
.brand-full{font-size:10.5px;margin-top:4px;letter-spacing:.3px;color:var(--brand-gray)}
.brand-url{font-size:11px;margin-top:5px;font-weight:600;color:var(--brand-gray);text-align:center}
</style>
</head>
<body>
<div class="banner">
  <div class="hero">
    <div class="hero-photo" role="img" aria-label="Modern city buildings along a river at sunset"></div>
    <div class="hero-text">
      <div class="line-a">JOIN OUR COLLABORATIVE</div>
      <div class="line-b">MULTICENTER SURGICAL OUTCOMES NETWORK</div>
      <div class="line-c">DATA FOR BETTER CARE</div>
    </div>
  </div>
  <div class="band">OUR GROUP QUALITIES</div>
  <div class="qualities">
    <div class="hex green hex-tight" style="left:19px;top:14px">Anesthesiologists /<br>Anesthesiology</div>
    <div class="hex gray" style="left:220px;top:11px">Research, Quality and Education</div>
    <div class="hex olive" style="left:117px;top:74px">Quality Champions</div>
    <div class="hex gray" style="left:17px;top:131px">Large data repository</div>
    <div class="hex orange" style="left:220px;top:131px">Medical Researchers</div>
    <div class="hex brown" style="left:117px;top:190px">Perioperative Outcomes</div>
    <div class="hex navy" style="left:17px;top:249px">Innovators and trailblazers</div>
    <div class="hex blue" style="left:220px;top:249px">Medical research</div>
  </div>
  <div class="footer">
    <div class="brand-mark"></div>
    <div class="brand-text">
      <div class="brand-name">TRVA</div>
      <div class="brand-full">CROSSWARD SURGICAL RESULTS ALLIANCE</div>
      <div class="brand-url">www.trva-net.org</div>
    </div>
  </div>
</div>
</body>
</html>
```